Rack Card Design for an Ayurvedic Beauty Product Project

Hello, I need to have rack cards. The rack cards would be about 3 products we are showcasing at an event. I am a cosmetic company. I have a logo and basic design ideas. I have attached some product images and info. By no means am I a designer so please excuse my messy AI files. Please feel free to design this as feminine as you like. :)

Target Market(s)

Beauty industry, organic, holistic, ayurveda

Industry/Entity Type

Cosmetic

```html
<!DOCTYPE html>
<html lang="en">
<head>
<meta charset="utf-8">
<title>Saffron Bloom Rack Card</title>
<link href="https://fonts.googleapis.com/css2?family=Open+Sans:wght@400;600;700&family=Montserrat:wght@600;700&display=swap" rel="stylesheet">
<style>
  :root {
    --bg: #e9e9ec;
    --paper: #ffffff;
    --plum: #8c1f68;
    --plum-deep: #6d154f;
    --magenta: #b02a7e;
    --blush: #f6c6d7;
    --blush-soft: #fbe3ec;
    --gold: #a8763a;
    --gold-light: #c99a5b;
    --ink: #2a2228;
  }
  * { box-sizing: border-box; margin: 0; padding: 0; }
  html, body { width: 1200px; height: 1177px; overflow: hidden; }
  body { background: var(--bg); font-family: "Open Sans", sans-serif; color: var(--ink); }

  .rack-card {
    position: absolute; left: 360px; top: 45px;
    width: 480px; height: 1087px;
    background: var(--paper);
    overflow: hidden;
    box-shadow: 0 6px 24px rgba(0,0,0,.12);
    padding-top: 48px;
  }
  .petal-wash {
    position: absolute; inset: 0 0 auto 0; height: 560px;
    background:
      radial-gradient(ellipse 60px 34px at 70px 40px, var(--blush) 0, transparent 100%),
      radial-gradient(ellipse 70px 36px at 400px 70px, var(--blush) 0, transparent 100%),
      radial-gradient(ellipse 50px 30px at 440px 200px, var(--blush-soft) 0, transparent 100%),
      radial-gradient(ellipse 60px 30px at 40px 170px, var(--blush-soft) 0, transparent 100%),
      radial-gradient(ellipse 200px 90px at 240px 470px, var(--blush-soft) 0, transparent 100%);
  }
  .content { position: relative; }

  .brand { display: flex; flex-direction: column; align-items: center; gap: 12px; }
  .brand-dot { width: 84px; height: 84px; border-radius: 50%; background: var(--gold-light); }
  .brand-name {
    font-family: "Montserrat", sans-serif; font-weight: 700; font-size: 19px;
    letter-spacing: 1.5px; color: var(--gold); line-height: 24px;
  }

  .about {
    margin: 18px auto 0; width: 404px;
    font-size: 12.4px; line-height: 1.18; text-align: justify; text-align-last: center;
  }

  .list-head { position: relative; margin-top: 20px; height: 34px; }
  .list-head::before {
    content: ""; position: absolute; left: 0; right: 0; top: 16px; height: 2px; background: var(--plum);
  }
  .list-title {
    position: relative; display: table; margin: 0 auto;
    padding: 8px 30px; border-radius: 20px;
    background: linear-gradient(180deg, var(--magenta), var(--plum-deep));
    color: #fff; font-family: "Montserrat", sans-serif; font-weight: 700; font-size: 14.5px;
    line-height: 18px; letter-spacing: .6px; white-space: nowrap;
  }

  .products { margin-top: 26px; padding: 0 18px; display: flex; flex-direction: column; gap: 16px; }
  .product { display: flex; align-items: center; gap: 18px; }
  .product-shot {
    flex: none; width: 122px; height: 122px; border-radius: 50%;
    border: 5px solid var(--gold);
    background: radial-gradient(circle at 50% 45%, #ffffff 0, #fbeef3 55%, #f2d9e3 100%);
    position: relative;
  }
  .product-shot::after {
    content: ""; position: absolute; left: 50%; top: 50%;
    width: 30px; height: 78px; transform: translate(-50%,-50%) rotate(10deg);
    border-radius: 6px 6px 4px 4px;
    background: linear-gradient(180deg, var(--plum) 0 82%, var(--gold-light) 82%);
  }
  .product-shot.jar::after {
    width: 58px; height: 64px; transform: translate(-50%,-50%); border-radius: 10px;
    background: linear-gradient(180deg, var(--plum) 0 30%, #f4f0f2 30%);
  }
  .product-name {
    font-family: "Montserrat", sans-serif; font-weight: 600; font-size: 13.5px;
    line-height: 17px; color: var(--plum); margin-bottom: 6px;
  }
  .product-copy { font-size: 12.8px; line-height: 1.17; text-align: justify; }

  .footer-photo {
    position: absolute; left: 0; bottom: 0; width: 100%; height: 215px;
    background: linear-gradient(180deg, rgba(255,255,255,0) 0, #f0a8c8 22%, #d64d98 58%, var(--plum) 100%);
  }
  .contact {
    position: absolute; left: 0; bottom: 46px; width: 100%;
    text-align: center; color: #fff; font-weight: 600;
  }
  .contact .phone { font-size: 20px; letter-spacing: 4px; margin-bottom: 6px; }
  .contact .web { font-size: 20px; letter-spacing: 3.5px; font-weight: 400; }
</style>
</head>
<body>
  <article class="rack-card">
    <div class="petal-wash" role="img" aria-label="Soft scattered pink rose petals"></div>
    <div class="footer-photo" role="img" aria-label="Close-up photo of pink rose petals"></div>

    <div class="content">
      <header class="brand">
        <span class="brand-dot"></span>
        <span class="brand-name">SAFFRON BLOOM</span>
      </header>

      <p class="about">Saffron Bloom curates organic infused products where holistic skin care meets a luxurious experience. Each ingredient is carefully selected; providing Ayurvedic herbs, rich minerals &amp; elements. Stimulating hydration and anti-oxidants to lift, firm and illuminate your skin. We believe in connecting with your inner mantra, stimulating higher vibrations, self-esteem, positive mind and soul. As a brand we work with our experts/suppliers of Ayurveda to ensure that our products meet the quality, wholesome healing that you need.</p>

      <div class="list-head">
        <h2 class="list-title">SAFFRON BLOOM PRODUCT LIST</h2>
      </div>

      <div class="products">
        <section class="product">
          <div class="product-shot" role="img" aria-label="Photo of the breast toner tube"></div>
          <div>
            <h3 class="product-name">Saffron Bloom Firming and Lifting Breast Toner</h3>
            <p class="product-copy">Using all natural Ayurvedic herbs, our breast toner, prepares the area for maximum absorption, giving you the best results and the most invigorating treatment</p>
          </div>
        </section>

        <section class="product">
          <div class="product-shot jar" role="img" aria-label="Photo of the breast cream jar"></div>
          <div>
            <h3 class="product-name">Saffron Bloom Firming and Lifting Breast Cream</h3>
            <p class="product-copy">Using all natural Ayurvedic herbs, our breast cream helps enhance, tighten, and lift your breast</p>
          </div>
        </section>

        <section class="product">
          <div class="product-shot" role="img" aria-label="Photo of the breast serum tube"></div>
          <div>
            <h3 class="product-name">Saffron Bloom Firming and Toning Breast Serum</h3>
            <p class="product-copy">Using all natural Ayurvedic herbs, and a touch of 24k gold, our serum enhances the experience and quality of results when partnered with the Saffron Bloom Firming and Lifting Breast Cream providing an all-day boosting experience</p>
          </div>
        </section>
      </div>
    </div>

    <footer class="contact">
      <p class="phone">555-014-2287</p>
      <p class="web">www.saffronbloom.com</p>
    </footer>
  </article>
</body>
</html>
```